Logo & Stationery Design for Non profit

This is  a nonprofit organization created to help minorities and seniors achieve financial freedom.  We want a logo that symbolizes hope and prosperity. 

Industry/Entity Type

Non Profit

Logo Text

Bright Harbor Foundation

Requirements
Must have
• The name "Bright Harbor Foundation"

```html
<!DOCTYPE html>
<html lang="en">
<head>
<meta charset="utf-8">
<title>Bright Harbor Foundation – Fax Cover</title>
<link href="https://fonts.googleapis.com/css2?family=Arimo:wght@400;700&display=swap" rel="stylesheet">
<style>
  :root {
    --ink: #000000;
    --paper: #ffffff;
  }
  html, body {
    margin: 0;
    padding: 0;
    width: 928px;
    height: 1200px;
    overflow: hidden;
    background: var(--paper);
  }
  .fax-sheet {
    position: relative;
    width: 928px;
    height: 1200px;
    background: var(--paper);
    color: var(--ink);
    font-family: "Arimo", Arial, sans-serif;
  }
  .brand-mark {
    position: absolute;
    left: 39px;
    top: 24px;
  }
  .brand-name {
    position: absolute;
    left: 164px;
    top: 54px;
    margin: 0;
    font-weight: 400;
    font-size: 47px;
    line-height: 1;
    letter-spacing: -1px;
    white-space: nowrap;
  }
  .brand-sub {
    position: absolute;
    left: 330px;
    top: 100px;
    margin: 0;
    font-weight: 400;
    font-size: 13px;
    letter-spacing: 3px;
    line-height: 1;
  }
  .sender-block {
    position: absolute;
    left: 51px;
    top: 161px;
    margin: 0;
    font-size: 17.5px;
    line-height: 27px;
    font-style: normal;
  }
  .doc-title {
    position: absolute;
    right: 32px;
    top: 245px;
    margin: 0;
    font-size: 54px;
    font-weight: 700;
    line-height: 1;
  }
  .rule-heavy {
    position: absolute;
    left: 36px;
    top: 299px;
    width: 860px;
    height: 5px;
    background: var(--ink);
  }
  .rule-light {
    position: absolute;
    left: 36px;
    top: 561px;
    width: 860px;
    height: 1.5px;
    background: var(--ink);
  }
  .field {
    position: absolute;
    margin: 0;
    font-size: 18px;
    line-height: 1;
  }
  .field-date { left: 495px; top: 344px; }
  .field-pages { left: 740px; top: 344px; }
  .field-to { left: 62px; top: 388px; }
  .field-from { left: 495px; top: 388px; }
  .field-fax { left: 62px; top: 434px; }
  .field-phone-from { left: 495px; top: 434px; }
  .field-phone-to { left: 62px; top: 480px; }
  .field-subject { left: 62px; top: 525px; }
  .field-comments { left: 54px; top: 574px; }
</style>
</head>
<body>
  <main class="fax-sheet">
    <header>
      <svg class="brand-mark" width="116" height="116" viewBox="0 0 116 116" aria-hidden="true">
        <circle cx="58" cy="58" r="56" fill="var(--ink)"/>
      </svg>
      <p class="brand-name">Bright Harbor</p>
      <p class="brand-sub">Foundation</p>

      <address class="sender-block">
        Bright Harbor Foundation building<br>
        Chicago, IL (000) 000-0000<br>
        Phone:(000) 000-0000<br>
        FAX:(000) 000-0000<br>
        www.bhf.org
      </address>

      <h1 class="doc-title">Fax</h1>
    </header>

    <div class="rule-heavy"></div>

    <section class="fax-fields">
      <p class="field field-date">Date:</p>
      <p class="field field-pages">#of pates:</p>
      <p class="field field-to">To:</p>
      <p class="field field-from">From:</p>
      <p class="field field-fax">Fax:</p>
      <p class="field field-phone-from">Telephone:</p>
      <p class="field field-phone-to">Telephone:</p>
      <p class="field field-subject">Subject:</p>
    </section>

    <div class="rule-light"></div>

    <p class="field field-comments">Comments:</p>
  </main>
</body>
</html>
```